Flyer for Cafe

We need a flyer to promote our menu..
I'd like to say:
-Burgers made to order
-Fresh Sandwiches and wraps daily
-Amazing coffee
-Hot Chips available (french fries.. we call them chips in Australia)
I have attached our logo below, and I have also attached a flyer that i like the look of..am wanting something similar.
Flyer to be one sided on A4 Paper
UPDATE:
I forgot to add our location...if we can put
"Located at The Pinecrest Uni Hospital"
"Open from 6am till 4pm. Monday - Friday"
Along the bottom of the flyer, with the contact details, can we please add an instagram icon and a like us on Facebook icon.
Target Market(s)
We are a cafe at a Hospital, so we target doctors, nurses.
We are also next to a university, so we are trying to attract students also
Industry/Entity Type
Cafe

```html
<!DOCTYPE html>
<html lang="en">
<head>
<meta charset="utf-8">
<title>Ward Bites Cafe Flyer</title>
<link rel="stylesheet" href="https://fonts.googleapis.com/css2?family=Archivo+Narrow:wght@700&family=Satisfy&display=swap">
<style>
  :root {
    --page-bg: #3e4f51;
    --stripe-orange: #f29a1c;
    --stripe-yellow: #f7c531;
    --panel-light: #dcdccb;
    --panel-mid: #a9a88e;
    --panel-dark: #8d8b72;
    --headline-red: #c8171e;
    --headline-edge: #ffe46a;
    --ribbon-red: #e0192f;
    --ribbon-yellow: #fff200;
    --white: #ffffff;
    --ink: #1b1b1b;
    --food-warm: #b8742c;
    --food-deep: #5a2a12;
    --chips-gold: #e7b43a;
  }
  * { box-sizing: border-box; margin: 0; padding: 0; }
  html, body {
    width: 1200px; height: 1200px; overflow: hidden;
    background: var(--page-bg);
  }
  .flyer {
    position: absolute; left: 205px; top: 40px;
    width: 790px; height: 1120px;
    background: repeating-linear-gradient(-45deg,
      var(--stripe-orange) 0 18px, var(--stripe-yellow) 18px 36px);
    box-shadow: 0 6px 22px rgba(0,0,0,.35);
  }
  .panel {
    position: absolute; left: 39px; top: 39px; right: 36px; bottom: 39px;
    border: 4px solid var(--white);
    overflow: hidden;
    background: radial-gradient(ellipse at 55% 55%, var(--panel-light) 0%, var(--panel-mid) 55%, var(--panel-dark) 100%);
    font-family: "Archivo Narrow", "Arial Narrow", sans-serif;
  }
  .headline {
    position: absolute; left: 0; right: 0; text-align: center;
    color: var(--headline-red); font-size: 50px; line-height: 1;
    text-shadow: 2px 2px 0 var(--headline-edge), -2px -2px 0 var(--headline-edge),
                 2px -2px 0 var(--headline-edge), -2px 2px 0 var(--headline-edge),
                 4px 5px 4px rgba(0,0,0,.35);
  }
  .headline--burgers { top: 66px; }
  .headline--sandwiches { top: 176px; }
  .headline--wraps { top: 256px; }
  .headline--coffee { top: 374px; }
  .ampersand {
    position: absolute; left: 0; right: 0; top: 226px; text-align: center;
    font-size: 42px; color: var(--ink); line-height: 1;
    text-shadow: 2px 2px 0 var(--white), -2px -2px 0 var(--white),
                 2px -2px 0 var(--white), -2px 2px 0 var(--white);
  }
  .food-photo {
    position: absolute; left: 67px; top: 476px; width: 622px; height: 302px;
    border-radius: 40px;
    background: radial-gradient(ellipse at 28% 62%, var(--food-deep) 0%, var(--food-warm) 38%, transparent 70%),
                radial-gradient(ellipse at 72% 40%, #6e2c1c 0%, #8a4a2a 30%, transparent 60%),
                radial-gradient(ellipse at 60% 78%, var(--chips-gold) 0%, transparent 45%);
  }
  .chips-strip {
    position: absolute; left: 0; right: 0; bottom: 0; height: 48px;
    background: linear-gradient(180deg, #f3cf63, var(--chips-gold) 60%, #c98c22);
  }
  .ribbon-group {
    position: absolute; left: -60px; top: 770px; width: 860px; height: 140px;
    transform: rotate(-11deg); transform-origin: 50% 50%;
  }
  .ribbon {
    position: absolute; left: 0; right: 0; top: 58px; height: 70px;
    background: var(--ribbon-red);
    box-shadow: 0 4px 8px rgba(0,0,0,.3);
  }
  .hot-chips {
    position: absolute; left: 300px; top: 0; font-size: 46px;
    color: var(--white); line-height: 1;
    -webkit-text-stroke: 2px var(--ink);
    text-shadow: 3px 3px 0 var(--ink);
  }
  .located-label {
    position: absolute; left: 385px; top: 52px;
    font-family: "Satisfy", cursive; font-size: 30px; color: var(--white);
  }
  .location-name {
    position: absolute; left: 330px; top: 90px;
    font-size: 28px; color: var(--ribbon-yellow); line-height: 1;
  }
  .brand-badge {
    position: absolute; left: 40px; top: 815px; width: 190px; height: 190px;
    border-radius: 50%; background: var(--white);
    border: 6px solid var(--ribbon-red);
    display: flex; align-items: center; justify-content: center;
  }
  .brand-name {
    font-size: 40px; color: var(--ribbon-red); line-height: 1; text-align: center;
  }
  .hours {
    position: absolute; left: 375px; top: 897px;
    color: var(--white); font-size: 23px; line-height: 1.55;
    text-shadow: 1px 1px 2px rgba(0,0,0,.4);
  }
</style>
</head>
<body>
  <main class="flyer">
    <div class="panel">
      <h1 class="headline headline--burgers">Burgers made to order</h1>
      <p class="headline headline--sandwiches">Fresh Sandwiches</p>
      <p class="ampersand">&amp;</p>
      <p class="headline headline--wraps">wraps daily</p>
      <p class="headline headline--coffee">Amazing coffee</p>

      <div class="food-photo" role="img" aria-label="Burger with lettuce, tomato and onion beside hot chips and a steaming cup of coffee"></div>

      <div class="chips-strip" role="img" aria-label="Close-up of golden hot chips"></div>

      <div class="ribbon-group">
        <div class="ribbon"></div>
        <p class="hot-chips">Hot Chips available</p>
        <p class="located-label">Located at</p>
        <p class="location-name">The Pinecrest Uni Hospital</p>
      </div>

      <div class="brand-badge">
        <span class="brand-name">Ward<br>Bites</span>
      </div>

      <p class="hours">Open from 6am till 4pm<br>Monday - Friday</p>
    </div>
  </main>
</body>
</html>
```